Voltarey - Flyer design

Description -
Motorhome and Caravan EWOFs
Recreational Vehicles (such as caravans, motorhomes, RVs, Boats etc) and Relocatable buildings that can be connected to an electricity supply must be regularly checked for electrical safety. An EWOF needs to be issued every 4 years.
Pre-purchase house inspections
A pre-purchase electrical inspection prior to buying a home can be used to identify any dangerous and unsafe electrical parts of the installation that may be costly to repair once the property has been purchased. Giving you peace of mind when buying your new home.
High risk Electrical inspections
All Prescribed Electrical Work that falls under the High Risk category must be inspected by a Registered Electrical Inspector and have a Record of Inspection certificate issued.
Electric Vehicle Chargers
Any electrical vehicle charger that can be accessed by the public (ie in a non-domestic situation) must be periodically inspected and certified every 12 months.
General Electrical Services
Domestic and commercial - We do new builds, Renovations, Maintenance and more!
Dean Fowler - Electrician and Electrical Inspector
Ph - 0227839152
Dean@voltarey.co.nz
Auckland
------
I also want there to be a few symbols similar to the files I have attached.
The main areas that I am hoping to find work is with caravans/motohomes and EV car chargers so these symbols are quite important.
Thanks so much

```html
<!DOCTYPE html>
<html lang="en">
<head>
<meta charset="utf-8">
<title>Voltarey – Electrical Safety Inspections Flyer</title>
<link rel="stylesheet" href="https://fonts.googleapis.com/css2?family=Oswald:wght@300;400;500&family=Open+Sans:wght@400;600;700&display=swap">
<style>
  :root {
    --green: #7dc242;
    --ink: #3a3a3a;
    --grey: #6f6f6f;
    --pill-border: #707070;
    --paper: #ffffff;
    --backdrop: #e4e5ea;
  }
  * { box-sizing: border-box; margin: 0; padding: 0; }
  html, body { width: 1200px; height: 856px; overflow: hidden; background: var(--backdrop); }
  .flyer {
    position: absolute; left: 310px; top: 18px; width: 580px; height: 820px;
    background: var(--paper); overflow: hidden;
    box-shadow: 0 4px 14px rgba(0,0,0,.18);
    font-family: "Open Sans", sans-serif;
  }
  .hero-photo {
    position: absolute; left: 0; top: 0; width: 580px; height: 230px;
    background:
      linear-gradient(180deg, rgba(125,194,66,0) 60%, var(--green) 100%),
      linear-gradient(90deg, #5f9a3c 0%, #7fae55 30%, #a9b3bf 52%, #3d4a63 68%, #b4553a 82%, #2f3b55 100%);
  }
  .title-band {
    position: absolute; left: 0; top: 226px; width: 580px; height: 96px; background: var(--green);
  }
  .headline {
    position: absolute; left: 0; top: 203px; width: 580px; text-align: center;
    font-family: "Oswald", sans-serif; font-weight: 500; color: #fff;
    font-size: 44px; line-height: 47px; letter-spacing: .2px;
  }
  .subhead {
    position: absolute; left: 0; top: 320px; width: 580px; text-align: center;
    font-family: "Oswald", sans-serif; font-weight: 300; color: var(--green);
    font-size: 31px; line-height: 34px; white-space: nowrap;
  }
  .intro {
    position: absolute; left: 0; top: 356px; width: 580px; text-align: center;
    font-family: "Oswald", sans-serif; font-weight: 400; color: var(--ink);
    font-size: 16.5px; line-height: 21.5px; white-space: nowrap;
  }
  .service {
    position: absolute; top: 422px; width: 174px; height: 289px;
    border: 4px solid var(--pill-border); border-radius: 87px;
    text-align: center; padding: 8px 8px 0;
  }
  .service--house { left: 19px; }
  .service--risk { left: 203px; height: 249px; }
  .service--ev { left: 388px; }
  .service-icon { display: block; margin: 0 auto; width: 62px; height: 62px; }
  .service-icon--placeholder { background: #e3f1d6; border-radius: 8px; }
  .service-title {
    margin-top: 16px; font-family: "Oswald", sans-serif; font-weight: 500;
    color: var(--green); font-size: 19.5px; line-height: 20px; white-space: nowrap;
  }
  .service-title .spaced { letter-spacing: 3.4px; }
  .service-text {
    margin-top: 3px; font-size: 9.6px; line-height: 13.6px; color: var(--grey);
    text-align: center; white-space: nowrap;
  }
  .service-text--tight { line-height: 11.6px; margin-top: 5px; }
  .extra-title {
    margin-top: 5px; font-weight: 700; color: var(--green); font-size: 10.5px; line-height: 13px; white-space: nowrap;
  }
  .extra-text { font-size: 9.6px; line-height: 11.6px; color: var(--grey); white-space: nowrap; }
  .brand {
    position: absolute; left: 216px; top: 690px; width: 150px; height: 46px;
    display: flex; align-items: center; gap: 8px;
  }
  .brand-square { width: 14px; height: 14px; background: var(--green); }
  .brand-name { font-size: 26px; font-weight: 600; color: var(--grey); letter-spacing: .3px; }
  .contact-name {
    position: absolute; left: 0; top: 740px; width: 580px; text-align: center;
    font-size: 13px; font-weight: 600; color: #222;
  }
  .contact-role {
    position: absolute; left: 0; top: 756px; width: 580px; text-align: center;
    font-size: 15px; font-weight: 700; color: #222;
  }
  .contact-band {
    position: absolute; left: 0; top: 780px; width: 580px; height: 40px;
    background: var(--green); display: flex; align-items: center; justify-content: center;
    font-size: 20px; font-weight: 700;
  }
  .contact-phone { color: #fff; }
  .contact-divider { width: 3px; height: 25px; background: #222; margin: 0 5px; }
  .contact-email { color: #6b6b6b; }
</style>
</head>
<body>
<main class="flyer">
  <div class="hero-photo" role="img" aria-label="Photo of a motorhome and caravan on grass beside a modern glass house at dusk, with an EV charger"></div>
  <div class="title-band"></div>
  <h1 class="headline">Electrical Safety Inspections<br>&amp; Certifications</h1>
  <h2 class="subhead">Homes, Motorhomes, and Electric Vehicle Chargers</h2>
  <p class="intro">Recreational Vehicles (such as caravans, motorhomes, RVs, Boats etc) and<br>Relocatable buildings that can be connected to an electricity supply must be<br>regularly checked for electrical safety. An EWOF needs to be issued every 4 years.</p>

  <section class="service service--house">
    <div class="service-icon service-icon--placeholder" role="img" aria-label="Icon of an electrician in a hard hat holding a multimeter"></div>
    <h3 class="service-title"><span class="spaced">Pre-purchase</span><br>house inspections</h3>
    <p class="service-text">A pre-purchase electrical<br>inspection prior to buying a<br>home can be used to identify<br>any dangerous and unsafe<br>electrical parts of the<br>installation that may be costly<br>to repair once the property<br>has been purchased. Giving<br>you peace of mind when<br>buying your new<br>home.</p>
  </section>

  <section class="service service--risk">
    <svg class="service-icon" viewBox="0 0 64 64" fill="none" stroke="#7dc242" stroke-width="2.2" stroke-linejoin="round" stroke-linecap="round" aria-hidden="true">
      <path d="M8 20 Q8 12 16 12 H50 Q58 12 58 22 V44 H8 Z"/>
      <rect x="14" y="19" width="18" height="10" rx="2"/>
      <rect x="42" y="20" width="9" height="22" rx="1"/>
      <path d="M8 36 H36"/>
      <circle cx="26" cy="47" r="5"/>
      <path d="M2 48 H8 M2 44 V52"/>
    </svg>
    <h3 class="service-title">High risk Electrical<br>inspections</h3>
    <p class="service-text">All Prescribed Electrical Work<br>that falls under the High Risk<br>category must be inspected by<br>a Registered Electrical<br>Inspector and have a<br>Record of Inspection<br>certificate issued.</p>
  </section>

  <section class="service service--ev">
    <svg class="service-icon" viewBox="0 0 64 64" fill="none" stroke="#7dc242" stroke-width="2.2" stroke-linecap="round" stroke-linejoin="round" aria-hidden="true">
      <path d="M50 16 A24 24 0 1 0 56 34"/>
      <path d="M48 10 l6 6 M52 8 h6 v6 M54 14 l3 3"/>
      <path d="M18 40 V34 l4-7 h18 l5 7 v6 Z"/>
      <circle cx="24" cy="41" r="3"/><circle cx="40" cy="41" r="3"/>
      <path d="M33 24 l-4 6 h5 l-3 6"/>
    </svg>
    <h3 class="service-title">Electric Vehicle<br>Chargers</h3>
    <p class="service-text service-text--tight">Any electrical vehicle charger<br>that can be accessed by the<br>public (ie in a non-domestic<br>situation) must be periodically<br>inspected and certified every 12<br>months.</p>
    <p class="extra-title">General Electrical Services</p>
    <p class="extra-text">Domestic and commercial<br>- We do new builds,<br>Renovations,<br>Maintenance and<br>more!</p>
  </section>

  <div class="brand"><span class="brand-square"></span><span class="brand-name">Voltarey</span></div>
  <p class="contact-name">Dean Fowler</p>
  <p class="contact-role">Electrician and Electrical Inspector</p>
  <footer class="contact-band">
    <span class="contact-phone">0227839152</span>
    <span class="contact-divider"></span>
    <span class="contact-email">Dean@voltarey.co.nz</span>
  </footer>
</main>
</body>
</html>
```